Letterhead and matching envelope design for a dental office

We need a new stationary design, letterhead and envelope #10, for a dental office in Denver area. We are called Brightfield Dental. We want a simple and minimalistic design but not a boring design. I wish to have one good point that makes it look professional. I have attached our logo. Feel free to use either one. I want the design for letterhead and envelope look like a "matching pair" but not look the same. The envelope doesn't have to be white and it will have an address window on bottom left.

Target Market(s)

everyone who visits dentist (adults)

Industry/Entity Type

Dental

Font styles to use
Other font styles liked:
• close to font on logo or something that matches well

Requirements
Must have
• professional
• simple, minimalistic
• unique point that stands out
Nice to have
• matching but not same design for letterhead and envelope
Should not have
• not look like all the other boring designs
• no flowery, distracting feats

```html
<!DOCTYPE html>
<html lang="en">
<head>
<meta charset="utf-8">
<title>Brightfield Dental – Letterhead &amp; Envelope</title>
<link rel="stylesheet" href="https://fonts.googleapis.com/css2?family=Montserrat:wght@500;600;700&family=Raleway:wght@300&display=swap">
<style>
  :root {
    --page-bg: #ffffff;
    --brand-green: #3f9a57;
    --headline-green: #8cc63f;
    --ink-grey: #6d7077;
    --ink-dark: #1d1d1f;
    --teal-light: #cfe9ea;
    --teal-mid: #8cc9d3;
    --teal-deep: #5aa9c2;
    --mint-wash: #e4f3ee;
    --stamp-tone: #d9c7a3;
    --signature-tone: #c9d6dd;
  }
  * { box-sizing: border-box; margin: 0; padding: 0; }
  html, body { width: 778px; height: 1200px; overflow: hidden; background: var(--page-bg); }
  body { position: relative; font-family: "Montserrat", Arial, sans-serif; }

  .letterhead {
    position: absolute; left: 77px; top: 30px; width: 625px; height: 807px;
    overflow: hidden; background: var(--page-bg);
  }
  .letterhead__backdrop, .envelope__backdrop { position: absolute; inset: 0; width: 100%; height: 100%; }

  .brand { position: absolute; left: 24px; top: 126px; text-align: center; width: 300px; }
  .brand__name {
    font-family: "Montserrat", Arial, sans-serif; font-weight: 600; font-size: 19px;
    letter-spacing: 1.5px; color: var(--brand-green); text-transform: uppercase;
  }
  .brand__place {
    margin-top: 2px; font-size: 10px; font-weight: 500; letter-spacing: 9px;
    color: var(--brand-green);
  }

  .contact { position: absolute; left: 400px; top: 60px; list-style: none; }
  .contact__item {
    display: flex; align-items: flex-start; gap: 6px; margin-bottom: 13px;
    font-size: 10.5px; font-weight: 700; color: var(--ink-grey); line-height: 13px;
  }
  .contact__item svg { flex: none; width: 11px; height: 11px; margin-top: 1px; fill: var(--ink-grey); }

  .letter { position: absolute; left: 87px; top: 238px; width: 492px; }
  .letter__headline {
    font-family: "Raleway", Arial, sans-serif; font-weight: 300; font-size: 38px;
    color: var(--headline-green); letter-spacing: 1px; line-height: 1; margin-bottom: 14px;
  }
  .letter__para {
    font-size: 11.6px; font-weight: 600; line-height: 18.4px; color: var(--ink-grey);
    margin-bottom: 17px;
  }

  .signature {
    position: absolute; left: 428px; top: 625px; width: 130px; height: 70px;
    border-radius: 35px; background: radial-gradient(ellipse at center, var(--signature-tone), transparent 70%);
  }
  .signatory {
    position: absolute; right: 40px; top: 705px;
    font-size: 13.5px; font-weight: 700; color: var(--ink-grey);
  }

  .envelope {
    position: absolute; left: 48px; top: 850px; width: 696px; height: 304px;
    overflow: hidden; background: var(--page-bg); border: 1px solid #c8d2d6;
  }
  .envelope__return {
    position: absolute; left: 26px; top: 40px;
    font-size: 11.5px; font-weight: 700; color: var(--ink-dark); line-height: 14.5px;
  }
  .envelope__stamp {
    position: absolute; left: 614px; top: 20px; width: 42px; height: 72px;
    background: linear-gradient(160deg, #efe3c9, var(--stamp-tone));
    border: 2px dashed #c9b48a;
  }
  .envelope__window {
    position: absolute; left: 63px; top: 183px; width: 331px; height: 84px;
    background: #ffffff; border-radius: 9px;
  }
</style>
</head>
<body>

<section class="letterhead">
  <svg class="letterhead__backdrop" viewBox="0 0 625 807" preserveAspectRatio="none" aria-hidden="true">
    <defs>
      <linearGradient id="wash" x1="0" y1="0" x2="1" y2="1">
        <stop offset="0" stop-color="#e3f2f0"/>
        <stop offset="0.45" stop-color="#ffffff"/>
        <stop offset="1" stop-color="#dff0ee"/>
      </linearGradient>
      <linearGradient id="topSweep" x1="0" y1="0" x2="1" y2="0">
        <stop offset="0" stop-color="#cfe9ea" stop-opacity="0.2"/>
        <stop offset="1" stop-color="#5aa9c2" stop-opacity="0.85"/>
      </linearGradient>
      <linearGradient id="bottomSweep" x1="0" y1="1" x2="1" y2="0">
        <stop offset="0" stop-color="#5aa9c2" stop-opacity="0.9"/>
        <stop offset="1" stop-color="#cfe9ea" stop-opacity="0.3"/>
      </linearGradient>
    </defs>
    <rect width="625" height="807" fill="url(#wash)"/>
    <path d="M0 0 H625 V150 C520 90 420 40 250 20 C150 10 60 12 0 20 Z" fill="url(#topSweep)" opacity="0.55"/>
    <path d="M330 0 H625 V110 C560 60 470 20 330 0 Z" fill="#8cc9d3" opacity="0.45"/>
    <path d="M480 0 L625 0 L625 70 Z" fill="#5aa9c2" opacity="0.5"/>
    <path d="M0 690 C150 660 360 700 625 640 V807 H0 Z" fill="#cfe9ea" opacity="0.7"/>
    <path d="M0 720 C200 690 380 760 625 700 V807 H0 Z" fill="url(#bottomSweep)" opacity="0.7"/>
    <path d="M0 760 C160 735 300 790 420 807 H0 Z" fill="#5aa9c2" opacity="0.55"/>
    <path d="M0 665 C180 640 420 690 625 650" stroke="#b9dcd6" stroke-width="1.5" fill="none"/>
    <path d="M0 672 C200 650 400 700 625 660" stroke="#cde7e1" stroke-width="1" fill="none"/>
  </svg>

  <header class="brand">
    <div class="brand__name">Brightfield Dental</div>
    <div class="brand__place">Lakeview</div>
  </header>

  <ul class="contact">
    <li class="contact__item">
      <svg viewBox="0 0 12 12"><rect x="0.5" y="2" width="11" height="8" rx="1"/></svg>
      www.brightfielddental.com
    </li>
    <li class="contact__item">
      <svg viewBox="0 0 12 12"><path d="M6 0.5a4 4 0 0 0-4 4c0 3 4 7 4 7s4-4 4-7a4 4 0 0 0-4-4zm0 5.5a1.5 1.5 0 1 1 0-3 1.5 1.5 0 0 1 0 3z"/></svg>
      <span>2250 Meadowlark Pkwy Suite 210<br>Lakeview , CO 80031</span>
    </li>
    <li class="contact__item">
      <svg viewBox="0 0 12 12"><path d="M2.5 0.8 4.3 0.5 5.4 3.2 4.2 4.3c0.6 1.4 1.8 2.6 3.2 3.3L8.6 6.5l2.7 1.1-0.3 1.8C10.8 10.5 9.9 11.2 9 11 4.7 10.2 1.6 7.1 0.9 2.9 0.8 1.9 1.5 1 2.5 0.8z"/></svg>
      (720) 555-0148
    </li>
  </ul>

  <article class="letter">
    <h1 class="letter__headline">HEADLINE</h1>
    <p class="letter__para">Lorem ipsum dolor sit amet, consectetur adipiscing elit. Fusce dignissim pretium consectetur. Curabitur tempor posuere massa in varius. Pellentesque viverra nibh eu vehicula mattis. Nullam porta facilisis justo, a feugiat dolor sodales sed. Vestibulum neque nisi, elementum tincidunt metus sit amet, egestas bibendum enim. Aenean a blandit elit, vel rutrum mi. Nunc dapibus turpis sed massa aliquet tincidunt.</p>
    <p class="letter__para">Pellentesque id neque ligula. Nullam posuere, ligula a mattis posuere, lacus nisl adipiscing nunc, eu congue justo est ut diam. Nam quam nibh, dignissim non consequat in, semper eget purus. Nulla arcu sapien, viverra vitae metus tempor, congue ornare diam.</p>
    <p class="letter__para">Pellentesque vel nibh tempus, ullamcorper tortor sed, bibendum augue. Phasellus sollicitudin justo et quam aliquam sollicitudin. Sed eget nibh mollis, mattis sem et, viverra nulla.</p>
  </article>

  <div class="signature" role="img" aria-label="Handwritten signature of the dentist"></div>
  <p class="signatory">Dr. Daniel Reyes Moreau, DDS</p>
</section>

<section class="envelope">
  <svg class="envelope__backdrop" viewBox="0 0 696 304" preserveAspectRatio="none" aria-hidden="true">
    <defs>
      <linearGradient id="envWash" x1="0" y1="0" x2="1" y2="1">
        <stop offset="0" stop-color="#ffffff"/>
        <stop offset="0.6" stop-color="#f3faf9"/>
        <stop offset="1" stop-color="#dcefee"/>
      </linearGradient>
    </defs>
    <rect width="696" height="304" fill="url(#envWash)"/>
    <path d="M0 190 C180 170 420 230 696 190 V304 H0 Z" fill="#cfe9ea" opacity="0.7"/>
    <path d="M0 230 C160 210 300 270 480 304 H0 Z" fill="#5aa9c2" opacity="0.5"/>
    <path d="M320 304 C450 260 580 250 696 230 V304 Z" fill="#8cc9d3" opacity="0.55"/>
    <path d="M0 178 C200 160 430 215 696 180" stroke="#b9dcd6" stroke-width="1.5" fill="none"/>
  </svg>

  <address class="envelope__return" style="font-style: normal;">
    Brightfield Dental<br>
    2250 Meadowlark Pkwy Suite 210<br>
    Lakeview , CO 80031
  </address>

  <div class="envelope__stamp" role="img" aria-label="Postage stamp"></div>
  <div class="envelope__window" aria-label="Address window"></div>
</section>

</body>
</html>
```